Northgate Process Solutions

8.5 x 11 flyer one or two sides is fine. This will be used for a trade show. See message for details

Target Market(s)

Refineries and Petrochemical plants

Industry/Entity Type

Oil

```html
<!DOCTYPE html>
<html lang="en">
<head>
<meta charset="utf-8">
<title>Northgate Process Solutions – Trade Show Flyer</title>
<link href="https://fonts.googleapis.com/css2?family=Roboto:ital,wght@0,300;0,400;0,700;1,400&family=Roboto+Condensed:wght@700&display=swap" rel="stylesheet">
<style>
  :root {
    --green: #2e7d4f;
    --green-dark: #24653f;
    --ink: #1d1d1b;
    --text: #2b2b2b;
    --paper: #f4f4f4;
    --white: #ffffff;
    --divider: #666666;
  }
  html, body { margin: 0; padding: 0; overflow: hidden; background: var(--white); }
  .flyer {
    position: relative;
    width: 867px;
    height: 1200px;
    overflow: hidden;
    background: var(--paper);
    font-family: "Roboto", Arial, sans-serif;
    color: var(--text);
  }
  .imagery { position: absolute; inset: 0; }
  .content {
    position: absolute;
    left: 15px;
    width: 520px;
    top: 0;
    text-align: center;
  }
  .brand {
    position: absolute;
    top: 72px;
    left: 0; right: 0;
    margin: 0;
    font-weight: 700;
    font-size: 44px;
    line-height: 52px;
    color: var(--ink);
  }
  .headline {
    position: absolute;
    top: 228px;
    left: 0; right: 0;
    margin: 0;
  }
  .headline__main {
    display: block;
    font-family: "Roboto Condensed", "Arial Narrow", sans-serif;
    font-weight: 700;
    font-size: 34px;
    line-height: 38px;
    color: var(--green);
  }
  .headline__sub {
    display: block;
    font-weight: 400;
    font-size: 21px;
    letter-spacing: 4.2px;
    line-height: 30px;
    color: var(--ink);
  }
  .categories {
    position: absolute;
    top: 316px;
    left: 0; right: 0;
    margin: 0;
    font-family: "Roboto Condensed", "Arial Narrow", sans-serif;
    font-weight: 700;
    font-size: 29px;
    line-height: 37px;
    color: var(--green);
  }
  .materials {
    position: absolute;
    top: 456px;
    left: 0; right: 0;
    margin: 0;
    padding: 0;
    list-style: none;
    font-weight: 300;
    font-size: 24px;
    line-height: 34.9px;
    color: var(--ink);
  }
  .materials__more { color: var(--green); font-weight: 400; }
  .tagline {
    position: absolute;
    top: 907px;
    left: 0; right: 0;
    margin: 0;
    font-style: italic;
    font-size: 24px;
    line-height: 34px;
    color: var(--ink);
  }
  .contact {
    position: absolute;
    top: 1076px;
    left: 80px;
    display: flex;
    align-items: center;
    gap: 20px;
    font-weight: 700;
    font-size: 19px;
    color: var(--green);
  }
  .contact__item { display: flex; align-items: center; gap: 9px; }
  .contact__divider { width: 2px; height: 44px; background: var(--divider); transform: skewX(-14deg); }
</style>
</head>
<body>
<div class="flyer">

  <svg class="imagery" width="867" height="1200" viewBox="0 0 867 1200">
    <defs>
      <clipPath id="arc-clip">
        <circle cx="1161" cy="597" r="706"/>
      </clipPath>
      <linearGradient id="oil-tone" x1="0" y1="0" x2="1" y2="1">
        <stop offset="0" stop-color="#d9a53a"/>
        <stop offset="0.5" stop-color="#a9a9a2"/>
        <stop offset="1" stop-color="#6d6f70"/>
      </linearGradient>
      <linearGradient id="barrel-tone" x1="0" y1="0" x2="0" y2="1">
        <stop offset="0" stop-color="#c9ccd0"/>
        <stop offset="0.3" stop-color="#24409a"/>
        <stop offset="0.8" stop-color="#1c2f78"/>
        <stop offset="1" stop-color="#8a8f94"/>
      </linearGradient>
      <linearGradient id="tank-tone" x1="0" y1="0" x2="0" y2="1">
        <stop offset="0" stop-color="#2b2f4f"/>
        <stop offset="0.45" stop-color="#5a4a3c"/>
        <stop offset="1" stop-color="#c9a27a"/>
      </linearGradient>
    </defs>

    <g clip-path="url(#arc-clip)">
      <polygon points="440,0 867,0 867,485 440,293" fill="url(#oil-tone)" role="img" aria-label="Photo: golden oil pouring from a bottle"/>
      <polygon points="440,293 867,485 867,722 440,909" fill="url(#barrel-tone)" role="img" aria-label="Photo: rows of blue steel drums on pallets in a warehouse"/>
      <polygon points="440,909 867,722 867,1200 440,1200" fill="url(#tank-tone)" role="img" aria-label="Photo: refinery storage tanks lit at night"/>
      <line x1="440" y1="293" x2="867" y2="485" stroke="var(--white)" stroke-width="7"/>
      <line x1="440" y1="909" x2="867" y2="722" stroke="var(--white)" stroke-width="7"/>
      <circle cx="1139" cy="594" r="322" fill="var(--green-dark)"/>
    </g>

    <circle cx="1161" cy="597" r="706" fill="none" stroke="var(--white)" stroke-width="8"/>
    <circle cx="1161" cy="597" r="714" fill="none" stroke="var(--green)" stroke-width="6"/>
    <circle cx="544" cy="167" r="11" fill="var(--green)"/>
    <circle cx="541" cy="1028" r="11" fill="var(--green)"/>
  </svg>

  <div class="content">
    <h1 class="brand">Northgate<br>Process Solutions</h1>

    <h2 class="headline">
      <span class="headline__main">YOUR STRATEGIC PARTNER</span>
      <span class="headline__sub">FOR PRODUCTIVE SOLUTIONS</span>
    </h2>

    <p class="categories">CO-PRODUCTS.<br>BY-PRODUCTS.<br>PROCESS RESIDUALS.</p>

    <ul class="materials">
      <li>Alcohols</li>
      <li>Asphalt Flux</li>
      <li>Bitumen</li>
      <li>Crude Oil</li>
      <li>Distillation Residue</li>
      <li>Distressed Material</li>
      <li>Fuels</li>
      <li>Glycols</li>
      <li>Petroleum Hydrocarbons</li>
      <li>Solvents</li>
      <li>Tank Bottoms</li>
      <li class="materials__more">And More!</li>
    </ul>

    <p class="tagline">Procurement of Process Residuals and<br>Off-Spec Material Worldwide<br>Your Trusted Partner for 26 Years!</p>
  </div>

  <div class="contact">
    <span class="contact__item">
      <svg width="22" height="22" viewBox="0 0 24 24" fill="none" stroke="currentColor" stroke-width="2" aria-hidden="true">
        <circle cx="12" cy="12" r="10"/>
        <ellipse cx="12" cy="12" rx="4.5" ry="10"/>
        <line x1="2" y1="12" x2="22" y2="12"/>
        <path d="M4 7h16M4 17h16"/>
      </svg>
      www.northgate-ps.com
    </span>
    <span class="contact__divider"></span>
    <span class="contact__item">
      <svg width="22" height="22" viewBox="0 0 24 24" aria-hidden="true">
        <path fill="currentColor" d="M6.6 10.8a15.1 15.1 0 0 0 6.6 6.6l2.2-2.2a1 1 0 0 1 1-.25 11.4 11.4 0 0 0 3.6.57 1 1 0 0 1 1 1V20a1 1 0 0 1-1 1A17 17 0 0 1 3 4a1 1 0 0 1 1-1h3.5a1 1 0 0 1 1 1c0 1.25.2 2.45.57 3.57a1 1 0 0 1-.25 1z"/>
      </svg>
      555-014-2600
    </span>
  </div>

</div>
</body>
</html>
```